Brell Harbor Company Business Cards

Front and Back Business Card - logo and text setup - cool design. I need workable photoshop or illustrator files so I can setup each employee card with design that is created
Updates

Hi everyone, thank you for the great entries. Please no more white and blue cards - there are so many already - black and silver only now please. thanks!

Target Market(s)

Construction Industry - Facility Managers

Industry/Entity Type

Construction

Contact Information for Business Card

I really like contemporary simplistic looks - clean neat....not opposed to seeing some black backrounds

Requirements
Must have
• Logo/website address with design on front only - www.brellharbor-example.com (logo attached)
• Back:
• Name/Title/Company Address/Phone/email address
Nice to have
• Cool design
Should not have
• Nothing gimmicky like Fire or Water - since we are a Fire Protection company - it has all been done

```html
<!DOCTYPE html>
<html lang="en">
<head>
<meta charset="utf-8">
<title>Brell Harbor Company Business Cards</title>
<link href="https://fonts.googleapis.com/css2?family=Montserrat:wght@300;400;500;800&display=swap" rel="stylesheet">
<style>
  :root {
    --black: #18181a;
    --black-soft: #222226;
    --steel-dark: #3f444b;
    --steel: #5b6169;
    --silver: #b9bdc3;
    --silver-light: #dfe1e4;
    --silver-pale: #eef0f2;
    --grey-text: #7a8088;
    --white: #ffffff;
    --page: #ffffff;
    --frame: #c4c7cb;
  }
  * { box-sizing: border-box; margin: 0; padding: 0; }
  html, body { width: 1200px; height: 1200px; overflow: hidden; background: var(--page); }
  body { position: relative; font-family: "Montserrat", sans-serif; }

  .card { position: absolute; width: 540px; height: 308px; overflow: hidden; }
  .card svg.shapes { position: absolute; inset: 0; width: 100%; height: 100%; }

  .front-band { left: 40px; top: 69px; background: var(--black-soft); }
  .front-diagonal { left: 620px; top: 69px; background: var(--silver-light); }
  .front-strip { left: 40px; top: 446px; background: var(--black); }
  .back-split { left: 620px; top: 446px; background: var(--silver-pale); border: 1px solid var(--frame); }
  .back-stripes { left: 330px; top: 823px; background: var(--silver-pale); border: 1px solid var(--frame); }

  .band-photo {
    position: absolute; left: 0; right: 0; top: 88px; height: 132px;
    background: linear-gradient(100deg, var(--steel-dark) 0%, var(--steel) 45%, var(--steel-dark) 100%);
  }

  .wordmark {
    position: absolute; color: var(--white); font-weight: 800;
    font-size: 42px; letter-spacing: -0.5px; line-height: 1; white-space: nowrap;
  }
  .website {
    position: absolute; color: var(--silver-light); font-weight: 400;
    font-size: 12.5px; letter-spacing: 3px; white-space: nowrap;
  }

  .front-band .wordmark { right: 30px; top: 118px; }
  .front-band .website { right: 30px; top: 176px; }

  .front-diagonal .wordmark { right: 34px; top: 118px; }
  .front-diagonal .website { right: 34px; top: 176px; }

  .front-strip .wordmark { left: 0; right: 0; top: 124px; text-align: center; }
  .front-strip .silver-strip { position: absolute; left: 0; right: 0; top: 256px; height: 32px; background: var(--silver); }
  .front-strip .website { left: 0; right: 0; top: 264px; text-align: center; color: var(--black); font-weight: 500; }

  .person { position: absolute; line-height: 1.05; }
  .person .first { font-weight: 300; font-size: 24px; letter-spacing: 5px; color: var(--black); display: block; }
  .person .last { font-weight: 800; font-size: 24px; letter-spacing: 5px; color: var(--black); display: block; }
  .person .title { font-weight: 400; font-size: 14px; letter-spacing: 2px; color: var(--grey-text); display: block; }

  .back-split .dark-half { position: absolute; left: 270px; top: 0; right: 0; bottom: 0; background: var(--black); }
  .back-split .icon-rail { position: absolute; left: 252px; top: 45px; width: 34px; height: 222px; background: var(--steel); }
  .back-split .person { left: 60px; top: 124px; }

  .contact { position: absolute; font-size: 13.5px; line-height: 1.3; white-space: nowrap; }
  .back-split .contact { color: var(--silver-light); left: 300px; }
  .back-stripes .contact { color: var(--black); left: 268px; }
  .icon { position: absolute; width: 18px; height: 18px; }

  .back-stripes .person { left: 236px; top: 34px; padding-left: 8px; border-left: 2px solid var(--black); }
  .back-stripes .person .first, .back-stripes .person .last { font-size: 22px; }
</style>
</head>
<body>

  <section class="card front-band" aria-label="Front, steel band">
    <svg class="shapes" viewBox="0 0 540 308">
      <g fill="var(--silver)">
        <rect x="0" y="58" width="266" height="4" rx="2"/>
        <rect x="0" y="75" width="188" height="2"/>
        <rect x="428" y="58" width="112" height="3"/>
        <rect x="356" y="75" width="184" height="2"/>
        <rect x="0" y="229" width="190" height="4" rx="2"/>
        <rect x="0" y="246" width="112" height="2"/>
        <rect x="360" y="231" width="180" height="2"/>
        <rect x="275" y="246" width="265" height="2"/>
      </g>
    </svg>
    <div class="band-photo" role="img" aria-label="Faint photograph of an embossed equipment plate"></div>
    <div class="wordmark">Brell Harbor</div>
    <div class="website">www.brellharbor-example.com</div>
  </section>

  <section class="card front-diagonal" aria-label="Front, diagonal stripes">
    <svg class="shapes" viewBox="0 0 540 308">
      <g fill="var(--black)">
        <polygon points="136,0 540,0 540,308 273,308"/>
        <polygon points="64,0 86,0 200,150 186,150"/>
        <polygon points="100,0 114,0 212,140 204,140"/>
        <polygon points="0,108 0,132 140,308 120,308"/>
        <polygon points="0,168 0,308 102,308"/>
      </g>
    </svg>
    <div class="wordmark">Brell Harbor</div>
    <div class="website">www.brellharbor-example.com</div>
  </section>

  <section class="card front-strip" aria-label="Front, silver strip">
    <div class="wordmark">Brell Harbor</div>
    <div class="silver-strip"></div>
    <div class="website">www.brellharbor-example.com</div>
  </section>

  <section class="card back-split" aria-label="Back, split layout">
    <div class="dark-half"></div>
    <div class="icon-rail"></div>
    <div class="person">
      <span class="first">MARLO</span>
      <span class="last">VENTON</span>
      <span class="title">Title</span>
    </div>

    <svg class="icon" style="left:260px;top:78px" viewBox="0 0 24 24" aria-hidden="true">
      <path fill="var(--white)" d="M6.6 10.8a15 15 0 0 0 6.6 6.6l2.2-2.2c.3-.3.7-.4 1-.2 1.1.4 2.3.6 3.6.6.6 0 1 .4 1 1V20c0 .6-.4 1-1 1A17 17 0 0 1 3 4c0-.6.4-1 1-1h3.5c.6 0 1 .4 1 1 0 1.3.2 2.5.6 3.6.1.3 0 .7-.2 1z"/>
    </svg>
    <div class="contact" style="top:76px">+18 2000 5550 0101<br>+18 2000 5550 0202</div>

    <svg class="icon" style="left:260px;top:140px" viewBox="0 0 24 24" aria-hidden="true">
      <rect x="2" y="5" width="20" height="14" fill="var(--white)"/>
      <path d="M2 5l10 8 10-8M2 19l7-7M22 19l-7-7" stroke="var(--steel)" stroke-width="1.6" fill="none"/>
    </svg>
    <div class="contact" style="top:140px">info@brellharbor-example.com</div>

    <svg class="icon" style="left:260px;top:206px" viewBox="0 0 24 24" aria-hidden="true">
      <path fill="var(--white)" d="M12 2a7 7 0 0 0-7 7c0 5.2 7 13 7 13s7-7.8 7-13a7 7 0 0 0-7-7zm0 9.5A2.5 2.5 0 1 1 12 6.5a2.5 2.5 0 0 1 0 5z"/>
    </svg>
    <div class="contact" style="top:198px">your city address<br>street location, ny city, usa</div>
  </section>

  <section class="card back-stripes" aria-label="Back, diagonal stripes">
    <svg class="shapes" viewBox="0 0 540 308">
      <g fill="var(--black)">
        <polygon points="6,0 18,0 154,210 142,210"/>
        <polygon points="26,0 34,0 160,196 152,196"/>
        <polygon points="0,32 0,60 136,228 146,214"/>
        <polygon points="0,150 0,172 118,308 190,308"/>
        <polygon points="0,200 0,308 94,308"/>
      </g>
    </svg>
    <div class="person">
      <span class="first">MARLO</span>
      <span class="last">VENTON</span>
      <span class="title">Title</span>
    </div>

    <svg class="icon" style="left:232px;top:158px" viewBox="0 0 24 24" aria-hidden="true">
      <path fill="var(--black)" d="M6.6 10.8a15 15 0 0 0 6.6 6.6l2.2-2.2c.3-.3.7-.4 1-.2 1.1.4 2.3.6 3.6.6.6 0 1 .4 1 1V20c0 .6-.4 1-1 1A17 17 0 0 1 3 4c0-.6.4-1 1-1h3.5c.6 0 1 .4 1 1 0 1.3.2 2.5.6 3.6.1.3 0 .7-.2 1z"/>
    </svg>
    <div class="contact" style="top:152px">+18 2000 5550 0101<br>+18 2000 5550 0202</div>

    <svg class="icon" style="left:232px;top:206px" viewBox="0 0 24 24" aria-hidden="true">
      <rect x="2" y="5" width="20" height="14" fill="var(--black)"/>
      <path d="M2 5l10 8 10-8M2 19l7-7M22 19l-7-7" stroke="var(--white)" stroke-width="1.6" fill="none"/>
    </svg>
    <div class="contact" style="top:206px">info@brellharbor-example.com</div>

    <svg class="icon" style="left:232px;top:242px" viewBox="0 0 24 24" aria-hidden="true">
      <path fill="var(--black)" d="M12 2a7 7 0 0 0-7 7c0 5.2 7 13 7 13s7-7.8 7-13a7 7 0 0 0-7-7zm0 9.5A2.5 2.5 0 1 1 12 6.5a2.5 2.5 0 0 1 0 5z"/>
    </svg>
    <div class="contact" style="top:236px">your city address<br>street location, ny city, usa</div>
  </section>

</body>
</html>
```